Customer Loyalty Card - Tourism - Tour Card

We would like to make a loyalty card for our tour business. If someone books 1 full priced tour they then get 10% off the 2nd tour and 10% off the 3rd tour and 15% off the 4th tour they do with us. All bookings must be booked directly with Kestrel Bay Wildlife Tours

View our website for design and colour ideas www.kestrelbaywildlifetours.com

Target Market(s)

People on holidays doing tours on Lord Howe Island

Industry/Entity Type

Travel

Contact Information for Business Card

www.kestrelbaywildlifetours.com
Im looking for a 1 sided card - if possible.

Phone, email and address are probably not really required. I will need to stamp the card once a tour has been booked and paid for. There is no name and position, its just a business card sized Loyalty Card.

Requirements
Must have
• Logo
• I will need to stamp the card once a tour has been booked and paid for.

```html
<!DOCTYPE html>
<html lang="en">
<head>
<meta charset="utf-8">
<title>Kestrel Bay Wildlife Tours – Loyalty Tour Card</title>
<link rel="stylesheet" href="https://fonts.googleapis.com/css2?family=Arimo:wght@400;700&display=swap">
<style>
  :root {
    --backdrop: #000000;
    --sky: #27a6df;
    --ocean: #1c5f9f;
    --brand: #1b6aaa;
    --paper: #ffffff;
    --ink-soft: #8a8f95;
  }
  html, body {
    margin: 0;
    padding: 0;
    width: 916px;
    height: 1200px;
    overflow: hidden;
    background: var(--backdrop);
    font-family: "Arimo", Arial, sans-serif;
  }
  .sheet { position: relative; width: 916px; height: 1200px; }
  .card {
    position: absolute;
    left: 127px;
    width: 681px;
    height: 389px;
    background: var(--paper);
    overflow: hidden;
  }
  .card--front { top: 116px; }
  .card--back { top: 708px; }
  .card__waves { position: absolute; inset: 0; width: 100%; height: 100%; }

  .heading { position: absolute; left: 35px; top: 30px; color: var(--paper); }
  .heading__title {
    margin: 0;
    font-size: 33px;
    font-weight: 700;
    letter-spacing: 0.5px;
    line-height: 1;
  }
  .heading__sub { margin: 6px 0 0; font-size: 19px; font-weight: 700; }

  .brand {
    position: absolute;
    display: flex;
    flex-direction: column;
    align-items: center;
    text-align: center;
    color: var(--brand);
    font-weight: 700;
  }
  .brand__square { background: var(--brand); border-radius: 10px; }
  .brand--front { left: 426px; top: 70px; width: 150px; }
  .brand--front .brand__square { width: 72px; height: 72px; }
  .brand--front .brand__name { margin-top: 10px; font-size: 17px; line-height: 1.2; }
  .brand--back { left: 405px; top: 26px; width: 220px; }
  .brand--back .brand__square { width: 88px; height: 88px; border-radius: 12px; }
  .brand--back .brand__name { margin-top: 10px; font-size: 21px; line-height: 1.2; }

  .contacts {
    position: absolute;
    left: 354px;
    top: 240px;
    margin: 0;
    padding: 0;
    list-style: none;
  }
  .contacts__item {
    display: flex;
    align-items: center;
    height: 27px;
    margin-bottom: 16px;
    font-size: 13px;
    color: var(--ink-soft);
  }
  .contacts__icon { width: 27px; height: 27px; margin-right: 16px; flex: none; }

  .stamps {
    position: absolute;
    left: 366px;
    top: 205px;
    display: flex;
    gap: 18px;
    margin: 0;
    padding: 0;
    list-style: none;
  }
  .stamps__slot {
    width: 62px;
    display: flex;
    flex-direction: column;
    align-items: center;
    text-align: center;
  }
  .stamps__circle {
    width: 56px;
    height: 56px;
    border-radius: 50%;
    border: 2px dashed var(--sky);
    box-sizing: border-box;
  }
  .stamps__tour {
    margin-top: 7px;
    font-size: 11px;
    font-weight: 700;
    color: var(--brand);
    letter-spacing: 0.5px;
  }
  .stamps__offer { margin-top: 2px; font-size: 11px; color: var(--ink-soft); }
  .terms {
    position: absolute;
    right: 20px;
    top: 338px;
    width: 270px;
    margin: 0;
    font-size: 11px;
    line-height: 1.35;
    text-align: right;
    color: var(--ink-soft);
  }
</style>
</head>
<body>
<main class="sheet">

  <section class="card card--front" aria-label="Card front">
    <svg class="card__waves" viewBox="0 0 681 389" preserveAspectRatio="none" aria-hidden="true">
      <path d="M430,0 H535 C300,25 95,160 50,389 H15 C55,160 230,40 430,0 Z" fill="var(--ocean)"/>
      <path d="M0,0 H420 C230,40 50,150 14,389 H0 Z" fill="var(--sky)" stroke="var(--paper)" stroke-width="6"/>
    </svg>

    <div class="heading">
      <h1 class="heading__title">TOUR CARD</h1>
      <p class="heading__sub">Loyalty Rewards</p>
    </div>

    <div class="brand brand--front">
      <div class="brand__square"></div>
      <div class="brand__name">Kestrel Bay<br>Wildlife Tours</div>
    </div>

    <ul class="contacts">
      <li class="contacts__item">
        <svg class="contacts__icon" viewBox="0 0 27 27" aria-hidden="true">
          <rect width="27" height="27" rx="4" fill="var(--sky)"/>
          <path d="M9,6 L12,6 L13,10 L11,11.5 C12,14 13.5,15.5 16,16.5 L17.5,14.5 L21,15.5 L21,18.5 C21,19.5 20,20.5 19,20.5 C12,20 7,15 6.5,8 C6.5,7 7.5,6 9,6 Z" fill="var(--paper)"/>
        </svg>
        +61 (0)400 555 018
      </li>
      <li class="contacts__item">
        <svg class="contacts__icon" viewBox="0 0 27 27" aria-hidden="true">
          <rect width="27" height="27" rx="4" fill="var(--sky)"/>
          <rect x="6" y="8" width="15" height="11" fill="var(--paper)"/>
          <path d="M6,8 L13.5,14 L21,8" fill="none" stroke="var(--sky)" stroke-width="1.5"/>
        </svg>
        YOUR EMAIL ADDRESS HERE
      </li>
      <li class="contacts__item">
        <svg class="contacts__icon" viewBox="0 0 27 27" aria-hidden="true">
          <rect width="27" height="27" rx="4" fill="var(--sky)"/>
          <g fill="none" stroke="var(--paper)" stroke-width="1.5">
            <circle cx="13.5" cy="13.5" r="7.5"/>
            <ellipse cx="13.5" cy="13.5" rx="3.2" ry="7.5"/>
            <line x1="6" y1="13.5" x2="21" y2="13.5"/>
          </g>
        </svg>
        www.kestrelbaywildlifetours.com
      </li>
    </ul>
  </section>

  <section class="card card--back" aria-label="Card back">
    <svg class="card__waves" viewBox="0 0 681 389" preserveAspectRatio="none" aria-hidden="true">
      <path d="M22,0 H80 C100,200 320,345 545,389 H470 C250,355 45,220 22,0 Z" fill="var(--ocean)"/>
      <path d="M0,0 H20 C40,215 245,350 462,389 H0 Z" fill="var(--sky)" stroke="var(--paper)" stroke-width="6"/>
    </svg>

    <div class="brand brand--back">
      <div class="brand__square"></div>
      <div class="brand__name">Kestrel Bay<br>Wildlife Tours</div>
    </div>

    <ol class="stamps" aria-label="Stamp a box for each paid tour">
      <li class="stamps__slot"><div class="stamps__circle"></div><div class="stamps__tour">TOUR 1</div><div class="stamps__offer">Full price</div></li>
      <li class="stamps__slot"><div class="stamps__circle"></div><div class="stamps__tour">TOUR 2</div><div class="stamps__offer">10% off</div></li>
      <li class="stamps__slot"><div class="stamps__circle"></div><div class="stamps__tour">TOUR 3</div><div class="stamps__offer">10% off</div></li>
      <li class="stamps__slot"><div class="stamps__circle"></div><div class="stamps__tour">TOUR 4</div><div class="stamps__offer">15% off</div></li>
    </ol>

    <p class="terms">Valid on bookings made directly with<br>Kestrel Bay Wildlife Tours</p>
  </section>

</main>
</body>
</html>
```